food delivery web site design

Currently we have a smartphone app (ios/android) that is being used by our clients to make orders to about 30 different restaurants.

We would like to extent this and have also a website that is able to mimic the same functionalities:
- register
- show restaurants based on the selected address
- make order to an restaurant
- being able to process orders for other registered users (please read the attached doc for complete info on this)

Take a look at the attached doc for more info.

```html
<!DOCTYPE html>
<html lang="ro">
<head>
<meta charset="utf-8">
<title>dishGo – Ți-e foame?</title>
<link href="https://fonts.googleapis.com/css2?family=Oswald:wght@400;500&family=Open+Sans:wght@400&display=swap" rel="stylesheet">
<style>
  :root{
    --red:#9b1408;
    --red-line:#c8321f;
    --brown:#2a1f1d;
    --yellow:#f3d660;
    --ink:#1d1d1d;
    --muted:#555;
    --tile:#1b1b1b;
    --footer:#222;
    --white:#fff;
  }
  *{box-sizing:border-box;margin:0;padding:0}
  html,body{width:1200px;height:1108px;overflow:hidden;background:var(--white)}
  body{position:relative;font-family:"Open Sans",sans-serif;color:var(--ink)}
  .hero-photo{position:absolute;left:0;top:0;width:1200px;height:580px;
    background:
      radial-gradient(ellipse 300px 160px at 260px 190px, rgba(240,200,140,.55), transparent 70%),
      radial-gradient(ellipse 260px 140px at 820px 200px, rgba(240,220,150,.6), transparent 70%),
      radial-gradient(ellipse 220px 120px at 1100px 320px, rgba(236,200,120,.55), transparent 70%),
      radial-gradient(ellipse 200px 120px at 60px 330px, rgba(200,140,150,.45), transparent 70%),
      linear-gradient(180deg,#d9cfcf 0%,#e9e0dc 45%,#f6efe9 80%,#fff 100%);}
  .topbar{position:absolute;left:0;top:51px;width:1200px;height:52px;background:var(--red);
    border-top:2px solid var(--red-line);border-bottom:2px solid var(--red-line)}
  .topbar .rule{position:absolute;height:0;border-top:2px solid rgba(255,255,255,.7);top:23px}
  .topbar .dots{position:absolute;left:610px;width:276px;top:24px;border-top:2px dotted rgba(255,255,255,.6)}
  .logo-tab{position:absolute;left:138px;top:0;width:158px;height:158px}
  .brand{position:absolute;left:163px;top:23px;width:110px;height:110px;border-radius:50%;
    background:var(--white);display:flex;align-items:center;justify-content:center;
    font-family:"Oswald",sans-serif;font-size:26px;color:var(--red)}
  .call{position:absolute;left:350px;top:62px;font-family:"Oswald",sans-serif;font-size:22px;letter-spacing:-.4px;color:var(--white);white-space:nowrap}
  .call .num{color:var(--yellow)}
  .call svg{vertical-align:-2px;margin:0 2px 0 4px}
  .auth{position:absolute;top:66px;font-family:"Oswald",sans-serif;font-size:16px;color:var(--white);display:flex;gap:6px;align-items:center}
  h1{position:absolute;left:138px;top:200px;font-family:"Oswald",sans-serif;font-weight:400;font-size:35px;color:var(--ink);letter-spacing:-.5px}
  .lead{position:absolute;left:138px;top:256px;font-size:20.5px;color:#2a2a2a}
  .search{position:absolute;left:138px;top:310px;width:924px;height:124px;background:var(--red);border-bottom:3px solid #e0a040}
  .search::before{content:"";position:absolute;inset:6px;border:1px solid rgba(255,255,255,.35)}
  .label{position:absolute;top:20px;font-family:"Oswald",sans-serif;font-weight:500;font-size:16px;color:var(--white)}
  .field{position:absolute;top:46px;height:51px;background:var(--white);font-family:"Oswald",sans-serif;
    font-size:18px;letter-spacing:-.2px;color:#555;padding-left:13px;line-height:51px;white-space:nowrap;overflow:hidden}
  .go{position:absolute;left:795px;top:46px;width:102px;height:51px;background:var(--yellow);color:var(--red);
    font-family:"Oswald",sans-serif;font-weight:500;font-size:15px;line-height:19px;text-align:center;padding-top:6px}
  .suggest{position:absolute;left:166px;top:407px;width:534px;background:var(--white);border:1px solid #ddd;border-top:none}
  .suggest li{list-style:none;height:50px;line-height:50px;padding:0 34px 0 13px;border-top:1px solid #ddd;
    font-family:"Oswald",sans-serif;font-size:18px;letter-spacing:-.2px;color:#555;position:relative;white-space:nowrap;overflow:hidden}
  .suggest li span{position:absolute;right:12px;top:0;color:var(--red);font-family:"Open Sans",sans-serif;font-size:15px}
  .divider{position:absolute;top:470px;height:4px;border-top:1px solid #aaa;border-bottom:1px solid #aaa}
  .grid{position:absolute;left:138px;top:518px;width:924px;display:grid;grid-template-columns:repeat(5,129px);
    grid-auto-rows:145px;column-gap:69px;row-gap:30px}
  .card .thumb{width:129px;height:102px;background:var(--tile)}
  .card .name{margin-top:8px;font-size:15px;line-height:20px;color:var(--ink);white-space:nowrap}
  .card .cat{font-size:10.5px;line-height:14px;color:var(--muted);letter-spacing:.4px;margin-top:1px;white-space:nowrap}
  .footer{position:absolute;left:0;top:1052px;width:1200px;height:56px;background:var(--footer);border-top:3px solid #333;
    color:#eee;font-size:12.5px}
  .footer nav{position:absolute;left:138px;top:17px}
  .footer nav a{color:#eee;text-decoration:none}
  .footer nav i{color:#666;font-style:normal;margin:0 8px}
  .footer .copy{position:absolute;right:138px;top:17px}
</style>
</head>
<body>
  <div class="hero-photo" role="img" aria-label="Blurred close-up photo of plated desserts with strawberries and custard"></div>

  <header>
    <div class="topbar">
      <div class="rule" style="left:0;width:138px"></div>
      <div class="rule" style="left:296px;width:38px"></div>
      <div class="dots"></div>
      <div class="rule" style="left:1063px;width:137px"></div>
    </div>
    <svg class="logo-tab" viewBox="0 0 158 158" aria-hidden="true">
      <polygon points="0,0 158,0 158,130 136,152 22,152 0,130" fill="#2a1f1d"/>
      <polyline points="6,128 26,146 132,146 152,128" fill="none" stroke="rgba(255,255,255,.4)" stroke-width="1"/>
    </svg>
    <div class="brand">dishGo</div>
    <div class="call">SUNĂ-NE LA<svg width="14" height="18" viewBox="0 0 14 18"><path d="M3 1l3 4-2 2c1 3 3 5 5 6l2-2 3 3-2 3C6 17 0 9 2 2z" fill="#f3d660"/></svg><span class="num">0700 123 456</span></div>
    <div class="auth" style="left:905px"><svg width="14" height="13" viewBox="0 0 14 13"><path d="M1 12V7c0-2 2-3 4-3h4V1l5 5-5 5V8H5c-2 0-3 1-4 4z" fill="#fff"/></svg>LOGIN</div>
    <div class="auth" style="left:980px"><svg width="16" height="13" viewBox="0 0 16 13"><circle cx="6" cy="4" r="3" fill="#fff"/><path d="M0 13c0-4 3-5 6-5s6 1 6 5z" fill="#fff"/><path d="M13 2v5M10.5 4.5h5" stroke="#fff" stroke-width="1.6"/></svg>SIGN IN</div>
  </header>

  <h1>ȚI-E FOAME ?</h1>
  <p class="lead">Comandă direct de pe mobil mancărurile favorite de la restaurantul tău preferat.</p>

  <form class="search">
    <div class="label" style="left:28px">INTRODU ADRESA</div>
    <div class="field" style="left:28px;width:534px">LOREM IPSUM DOLOR SIT AMET, CONSECTETUER ADIPISCING ELIT. AENEAN</div>
    <div class="label" style="left:581px">ALEGE ORAȘUL</div>
    <div class="field" style="left:581px;width:196px">BUCUREȘTI
      <svg style="position:absolute;right:15px;top:21px" width="12" height="9" viewBox="0 0 12 9"><path d="M0 0h12L6 9z" fill="#555"/></svg>
    </div>
    <div class="go">AFIȘEAZĂ<br>RESTAURANTE</div>
  </form>

  <div class="divider" style="left:138px;width:28px"></div>
  <div class="divider" style="left:705px;width:357px"></div>

  <ul class="suggest">
    <li>ILLUM MALLEM LEVARES, QUO OPTIMUM ATQUE HUMANISSIMUM VIRUM<span>✕</span></li>
    <li>AB HOC AUTEM QUAEDAM NON MELIUS QUAM VETERES, QUAEDAM<span>✕</span></li>
  </ul>

  <main class="grid">
    <div class="card"><div class="thumb"></div><div class="name">La Ceaunul Vechi</div><div class="cat">ROMANESC</div></div>
    <div class="card"><div class="thumb"></div><div class="name">Casa Verdina</div><div class="cat">ITALIAN</div></div>
    <div class="card"><div class="thumb"></div><div class="name">the PAINTER</div><div class="cat">CONTEMPORAN</div></div>
    <div class="card"><div class="thumb"></div><div class="name">Morettino</div><div class="cat">ITALIAN</div></div>
    <div class="card"><div class="thumb"></div><div class="name">Clarissa</div><div class="cat">MIXT</div></div>
    <div class="card"><div class="thumb"></div><div class="name">Stone Road Cafe</div><div class="cat">AMERICAN, EUROPEAN</div></div>
    <div class="card"><div class="thumb"></div><div class="name">Boviluu</div><div class="cat">GRILL</div></div>
    <div class="card"><div class="thumb"></div><div class="name">Orbo Coffee Shop</div><div class="cat">CAFENEA</div></div>
    <div class="card"><div class="thumb"></div><div class="name">Zafferano Ristorante</div><div class="cat">ITALIAN</div></div>
    <div class="card"><div class="thumb"></div><div class="name">Chaudron Bistro</div><div class="cat">FRANCEZ</div></div>
    <div class="card"><div class="thumb"></div><div class="name">Butoiul cu Bere</div><div class="cat">ROMANESC</div></div>
    <div class="card"><div class="thumb"></div><div class="name">ONDA</div><div class="cat">SPANIOL</div></div>
    <div class="card"><div class="thumb"></div><div class="name">Zorel</div><div class="cat">ROMANESC</div></div>
    <div class="card"><div class="thumb"></div><div class="name">Gradina Lorena</div><div class="cat">VEGETARIAN</div></div>
    <div class="card"><div class="thumb"></div><div class="name">Sintra</div><div class="cat">CAFENEA</div></div>
  </main>

  <footer class="footer">
    <nav><a href="#">Contactează-ne</a><i>|</i><a href="#">Despre noi</a><i>|</i><a href="#">Parteneriii noștri</a><i>|</i><a href="#">FAQ</a><i>|</i><a href="#">Devino partener</a></nav>
    <div class="copy">Copyright © 2013 dishGo.ro. Toate drepturile rezervate.</div>
  </footer>
</body>
</html>
```